TIKLOOMTOT WEBSITE DESIGN

We need a website design based on the template- http://varolapixels.com/themes/quartzpage-bootstrap-wordpress-theme/. We purchased template and will build the website using wordpress. It is one page application. We wanted to list all content in one page and make it browser friendly (can be viewed in cell phone, pc, mac, ipad, etc).

The target audience is parents with babies/kids age from 0-5 year old. We wanted to sell the subscription based monthly boxes to the families. The box will include books, toys, crafts, kids consumer products and letter/note/card to the family from the experts. All boxes are customized based on children's age, gender and interests.

We wanted the site main color to be blue.

Please refer to these websites for ideas.
froxi.com
wwws.pebbleharbor.com
http://www.wigglyoats.com/

I've updated the project brief and make the project fund guaranteed. Thanks!

Target Market(s)

Parents with kids age from 0-5 years old. Mainly target to the China market.

Industry/Entity Type

Cell Phone

Colors
3277b5
85abd2
85cae6
33a6d7
0592cd
0355a3
ceddec
cee9f5

Requirements
Must have
• Must provide the design based on the template- http://varolapixels.com/themes/quartzpage-bootstrap-wordpress-theme/.
The site has to be Chinese character friendly since we are going to post Chinese content on the website. No English content.
The registration forms needs to be designed and include in the final deliverable.

```html
<!DOCTYPE html>
<html lang="en">
<head>
<meta charset="utf-8">
<title>TIKLOOMTOT</title>
<link href="https://fonts.googleapis.com/css2?family=Roboto:wght@400;500;700&family=Oswald:wght@500&family=Rubik:wght@700&display=swap" rel="stylesheet">
<style>
:root{
  --pink:#e2135b;
  --navy:#1f2c7c;
  --btn:#2b3b9c;
  --ink:#333;
  --dark:#363636;
  --darker:#2e2e2e;
  --gold:#f3b400;
  --red:#ea1c2c;
}
*{box-sizing:border-box;margin:0;padding:0}
html,body{width:724px;height:1200px;overflow:hidden}
body{position:relative;font-family:"Roboto",Arial,sans-serif;color:var(--ink);background:#fff}
.abs{position:absolute}
/* header */
.header{left:0;top:0;width:724px;height:83px;background:linear-gradient(90deg,#f6f1e3,#fbf7ec 50%,#f6f1e3)}
.brand-logo{left:106px;top:36px;width:80px;display:flex;align-items:center;gap:4px}
.brand-logo .dot{flex:none;width:10px;height:10px;border-radius:50%;background:var(--pink)}
.brand-logo span{font:700 8.5px "Roboto",sans-serif;color:var(--pink);white-space:nowrap}
.brand-tab{left:190px;top:0;width:95px;height:83px;background:var(--pink);color:#fff;font:500 9.5px "Roboto",sans-serif;display:flex;align-items:center;justify-content:center;letter-spacing:.2px}
.nav{left:285px;top:0;width:281px;height:83px;background:linear-gradient(180deg,#fbf0c2,#fcefb6);display:flex;align-items:center;justify-content:space-around;padding:0 8px;font-size:8px;color:#333}
.chat{left:570px;top:28px;width:60px;text-align:center;font-size:9px;color:#222}
.chat .ic{display:block;margin:0 auto 4px;width:13px;height:13px;border-radius:50%;background:#222}
/* hero */
.hero{left:0;top:83px;width:724px;height:321px;background:radial-gradient(ellipse at 45% 55%,#ffffff 0%,#eaf4fc 40%,#bfe0f7 100%)}
.hero h1{left:150px;top:76px;font:700 24px "Rubik",sans-serif;color:#d81b5f;letter-spacing:.5px}
.hero p{left:150px;top:113px;width:270px;font:700 11.5px/18px "Roboto",sans-serif;color:#333}
.hero .btn{left:150px;top:159px;width:84px;height:22px;background:var(--btn);color:#fff;font:700 8px/22px "Roboto",sans-serif;padding-left:11px;clip-path:polygon(0 0,88% 0,100% 50%,88% 100%,0 100%);box-shadow:0 3px 4px rgba(0,0,0,.2)}
.hero .arrow{top:150px}
.ph-box{left:316px;top:158px;width:110px;height:114px;border-radius:3px;background:linear-gradient(180deg,#3f93dd,#2f78c6);box-shadow:0 8px 10px -6px rgba(0,0,0,.35)}
.ph-bear{left:420px;top:0;width:224px;height:321px;background:radial-gradient(ellipse 46% 44% at 55% 52%,#a9cff0 0%,#9cc6ec 55%,rgba(191,224,247,0) 100%)}
/* about */
.about-title{left:0;top:420px;width:724px;text-align:center;font:500 22px "Oswald",sans-serif;color:var(--navy)}
.about-text{left:102px;top:456px;width:520px;text-align:center;font-size:7.3px;line-height:16.8px;color:#333}
/* experts */
.experts{left:0;top:547px;width:724px;height:215px;background:radial-gradient(ellipse at 50% 40%,#fffdf6,#f6eccb)}
.expert{top:32px;width:130px;text-align:center}
.expert .pic{width:90px;height:90px;margin:0 auto;border-radius:50%;border:2px solid #fff;box-shadow:0 0 0 1px #cfcfcf,0 2px 5px rgba(0,0,0,.2);background:radial-gradient(circle at 50% 45%,#c9b3a3,#8f7d70 75%)}
.expert h3{margin-top:18px;font:400 9px "Roboto",sans-serif;color:var(--pink)}
.expert p{margin-top:14px;font-size:7.6px;line-height:13px;color:#333}
/* shop */
.shop{left:0;top:762px;width:724px;height:236px;background:var(--dark)}
.photo{top:18px;width:162px;height:127px;border:3px solid #fff}
.photo.pink{left:106px;background:linear-gradient(135deg,#f3c7d4,#e8a7bb 50%,#d9d3cc)}
.photo.blue{left:278px;background:linear-gradient(135deg,#a8bfe0,#8ea9cf 50%,#e9e2d8)}
.card-title{top:157px;font:500 8.5px "Roboto",sans-serif;color:var(--gold)}
.card-text{top:171px;width:158px;font-size:5.8px;line-height:9px;color:#eee;text-align:justify}
.order{left:462px;top:14px;width:163px;height:208px;background:linear-gradient(180deg,#d8d8d8,#bdbdbd);border-radius:2px}
.order-head{left:-4px;top:6px;width:171px;height:26px;background:linear-gradient(180deg,#f23a3a,var(--red));color:#fff;text-align:center;font:500 11px/26px "Oswald",sans-serif}
.field{left:20px;width:128px;height:14px;background:#fff;border:1px solid #ccc;font-size:5.5px;line-height:12px;padding-left:4px;color:#666}
.order-btn{left:46px;top:182px;width:70px;height:17px;background:#d41a28;border-radius:2px;color:#fff;font-size:7px;line-height:17px;text-align:center}
/* info */
.info{left:0;top:998px;width:724px;height:116px;background:radial-gradient(ellipse at 45% 50%,#8fc6e8,#4d9ad3 60%,#3b86c4)}
.info h4{top:19px;font:400 11.5px "Roboto",sans-serif;color:#fff}
.info hr{position:absolute;top:34px;border:0;border-top:1px solid rgba(255,255,255,.6)}
.info .txt{font-size:7px;line-height:13px;color:#f1f8ff}
.mail{left:462px;top:74px;width:127px;height:19px;background:#fff;font-size:7px;line-height:19px;padding-left:7px;color:#888}
.join{left:589px;top:74px;width:32px;height:19px;background:#1a2f78;color:#fff;font:700 7px/19px "Roboto",sans-serif;text-align:center}
/* footer */
.footer{left:0;top:1114px;width:724px;height:86px;background:var(--darker)}
.footer .links{left:109px;top:32px;font-size:8.5px;color:#fff;letter-spacing:.2px}
.footer .copy{left:109px;top:51px;font-size:6px;color:#fff}
.footer .sn{left:422px;top:33px;font-size:8.5px;color:#fff}
.footer .sn-sub{left:422px;top:53px;font-size:6px;color:#fff}
.social{top:31px;width:22px;height:22px;border-radius:50%;background:#fff}
</style>
</head>
<body>
<header class="header abs">
  <div class="brand-logo abs"><span class="dot"></span><span>TIKLOOMTOT</span></div>
  <div class="brand-tab abs">TIKLOOMTOT</div>
  <nav class="nav abs"><span>ORDER NOW</span><span>ABOUT US</span><span>OUR EXPERTS</span><span>FAQ</span><span>SHARE</span></nav>
  <div class="chat abs"><span class="ic"></span>CHATLINE</div>
</header>

<section class="hero abs">
  <div class="ph-bear abs" role="img" aria-label="Soft blue plush teddy bear"></div>
  <div class="ph-box abs" role="img" aria-label="Colourful toy activity box"></div>
  <h1 class="abs">TIKLOOMTOT</h1>
  <p class="abs">Lorem Ipsum is simply dummy text of the printing and typesetting industry</p>
  <div class="btn abs">READ MORE &#9656;</div>
  <svg class="arrow abs" style="left:66px" width="16" height="28" viewBox="0 0 16 28"><path d="M14 2 2 14l12 12" fill="none" stroke="#222" stroke-width="2"/></svg>
  <svg class="arrow abs" style="left:644px" width="16" height="28" viewBox="0 0 16 28"><path d="M2 2l12 12L2 26" fill="none" stroke="#222" stroke-width="2"/></svg>
</section>

<h2 class="about-title abs">ABOUT US</h2>
<p class="about-text abs">Little Reader Box Club - let the children stay at home and enjoy the best the United States early education and childcare philosophy platform. Subscribe now to our monthly mysterious parcel, father and mother and baby can get US experts recommended books and American original award-winning early childhood reading experience, cultivate good habits of children everyday, as well as the latest toys handmade infant mental development. Mom and Dad will gain double surprise.</p>

<section class="experts abs">
  <div class="expert abs" style="left:101px"><div class="pic" role="img" aria-label="Portrait of expert"></div><h3>WEN HAOLIN, MD</h3><p>Lakeside General Hospital<br>pediatrician and physician</p></div>
  <div class="expert abs" style="left:232px"><div class="pic" role="img" aria-label="Portrait of expert"></div><h3>DR. OWEN R. HARTLEY</h3><p>Lakeside General Hospital<br>pediatrician and physician</p></div>
  <div class="expert abs" style="left:365px"><div class="pic" role="img" aria-label="Portrait of expert"></div><h3>ELISE NORBURY</h3><p>Lakeside General Hospital<br>pediatrician and physician</p></div>
  <div class="expert abs" style="left:497px"><div class="pic" role="img" aria-label="Portrait of expert"></div><h3>TAO MINGSHENG</h3><p>Lakeside General Hospital<br>pediatrician and physician</p></div>
</section>

<section class="shop abs">
  <div class="photo pink abs" role="img" aria-label="Pink plush bear in an opened gift box with toys"></div>
  <div class="photo blue abs" role="img" aria-label="Blue plush bear in an opened gift box with books"></div>
  <h3 class="card-title abs" style="left:106px">IPSUM IS SIMPLY DUMMY TEXT</h3>
  <p class="card-text abs" style="left:106px">Lorem Ipsum has been the industry's standard dummy text ever since the 1500s, when an unknown printer took a galley of type and scrambled it to make a type specimen book. It has survived not only five centuries</p>
  <h3 class="card-title abs" style="left:278px">IPSUM IS SIMPLY DUMMY TEXT</h3>
  <p class="card-text abs" style="left:278px">Lorem Ipsum has been the industry's standard dummy text ever since the 1500s, when an unknown printer took a galley of type and scrambled it to make a type specimen book. It has survived not only five centuries</p>
  <form class="order abs">
    <div class="order-head abs">ORDER NOW</div>
    <div class="field abs" style="top:37px">Child name</div>
    <div class="field abs" style="top:57px">Gender</div>
    <div class="field abs" style="top:77px">Birth date</div>
    <div class="field abs" style="top:97px">Your email</div>
    <div class="field abs" style="top:118px">Address</div>
    <div class="field abs" style="top:138px">Cell phone</div>
    <div class="field abs" style="top:158px">Choose plan: 6 month | 1 Year</div>
    <svg class="abs" style="left:139px;top:163px" width="7" height="5" viewBox="0 0 7 5"><path d="M0 0l3.5 4L7 0" fill="none" stroke="#888"/></svg>
    <div class="order-btn abs">ORDER NOW</div>
  </form>
</section>

<section class="info abs">
  <h4 class="abs" style="left:107px">LATEST NEWS</h4><hr style="left:107px;width:155px">
  <div class="txt abs" style="left:107px;top:39px;width:155px">27/JULY/2014<br>Donec consectetur diam ac nibh auctor ultricies. Integer mauris lacus, consequat in luctus id, semper sed felis. Cum sociis natoque penatibus<br><span style="margin-left:108px;font-size:6px">READ MORE &raquo;</span></div>
  <h4 class="abs" style="left:294px">GET IN TOUCH</h4><hr style="left:294px;width:124px">
  <div class="txt abs" style="left:297px;top:47px;line-height:16.5px">48 Maple Row, Brookfield, ON, Canada<br>Phone 555-014-2290<br>Email: hello@tikloomtot.com</div>
  <h4 class="abs" style="left:462px">NEWSLETTER</h4><hr style="left:462px;width:162px">
  <div class="txt abs" style="left:461px;top:41px;width:165px">Join our mailing list to stay up to date and get notices about our new releases!</div>
  <div class="mail abs">mail@example.com</div>
  <div class="join abs">JOIN</div>
</section>

<footer class="footer abs">
  <div class="links abs">HOME &nbsp;|&nbsp; ABOUT &nbsp;|&nbsp; PRODUCTS &nbsp;|&nbsp; BLOG &nbsp;|&nbsp; CONTACTS</div>
  <div class="copy abs">© 2014 Privacy Policy</div>
  <div class="sn abs">SOCIAL NETWORKS</div>
  <div class="sn-sub abs">Bayarsety kertya aset aplicaboes</div>
  <span class="social abs" style="left:524px"></span>
  <span class="social abs" style="left:551px"></span>
  <span class="social abs" style="left:578px"></span>
  <span class="social abs" style="left:605px"></span>
</footer>
</body>
</html>
```